Bramblewood Outings brochure

We need a brochure designed that is modern, high impact and grabs potential customers attention. I have provided a draft mock brochure as an example and to provide the desired information. The lay out and design can be changed.

The front to include image (examples provided. I may provide other images if I can source) Logo, Joining the Community, and perhaps a Community Access and Lifestyle Support Service, Specialising in Lifestyle and Recreation

Refer to website for information on the service www.bramblewoodoutings.com.au

Use colours of logo for design

Target Market(s)

CWPA participants (People with a disability and their family)

Colors

Designer to choose colors to be used in the design.

Requirements
Must have
• Image/s of people, logo, text in mock up design. Example images provided. Will source more images and upload.
Nice to have
• More than one image

```html
<!DOCTYPE html>
<html lang="en">
<head>
<meta charset="utf-8">
<title>Bramblewood Outings Brochure</title>
<link href="https://fonts.googleapis.com/css2?family=Montserrat:ital,wght@1,800&family=Open+Sans:ital,wght@0,400;0,700;1,700&display=swap" rel="stylesheet">
<style>
  :root {
    --green-tab: #7cc142;
    --green-head: #2aa64a;
    --text-grey: #555a56;
    --text-dark: #3d403e;
    --white: #ffffff;
    --warm-top: #fde9a6;
  }
  * { margin: 0; padding: 0; box-sizing: border-box; }
  html, body { width: 1200px; height: 849px; overflow: hidden; background: var(--white); }
  .brochure {
    position: relative; width: 1200px; height: 849px; overflow: hidden;
    font-family: "Open Sans", Arial, sans-serif; color: var(--text-grey);
    background: linear-gradient(180deg, var(--warm-top) 0%, #fdf5d6 12%, #ffffff 26%);
  }
  .photo-backdrop {
    position: absolute; left: 0; top: 80px; width: 1200px; height: 769px;
    background:
      radial-gradient(ellipse 360px 320px at 330px 380px, rgba(150,170,140,.35), transparent 70%),
      radial-gradient(ellipse 320px 300px at 720px 330px, rgba(170,185,160,.35), transparent 70%),
      radial-gradient(ellipse 300px 360px at 1050px 450px, rgba(160,178,150,.3), transparent 70%),
      radial-gradient(ellipse 500px 260px at 600px 760px, rgba(140,160,130,.3), transparent 70%);
  }
  .tab {
    position: absolute; height: 70px; width: 360px;
    background: var(--green-tab); border-radius: 26px 0 26px 0;
    display: flex; align-items: center; justify-content: center;
    font-family: "Montserrat", Arial, sans-serif; font-style: italic; font-weight: 800;
    color: var(--white); font-size: 32px; letter-spacing: .3px; text-align: center; line-height: 1.05;
  }
  .tab--two-line { font-size: 27px; }
  .body-text { position: absolute; font-size: 13px; line-height: 20px; letter-spacing: .4px; }
  .sub-head { position: absolute; color: var(--green-head); font-weight: 700; font-size: 18.5px; line-height: 22px; }
  .bullets { position: absolute; list-style: none; font-size: 13px; line-height: 20px; letter-spacing: .3px; }
  .bullets li { padding-left: 10px; text-indent: -10px; }
  .bullets li::before { content: "• "; }
  .value-title { position: absolute; left: 421px; width: 360px; text-align: center; color: var(--green-head); font-weight: 700; font-size: 24px; letter-spacing: 1.5px; }
  .value-text { position: absolute; left: 436px; width: 330px; text-align: center; font-size: 15px; line-height: 22px; letter-spacing: .3px; }
  .note { position: absolute; font-style: italic; font-weight: 700; font-size: 12.5px; line-height: 18px; color: var(--text-dark); }
  .apply-text { position: absolute; font-weight: 700; font-size: 12.5px; line-height: 18px; color: var(--text-dark); }
  .brand { position: absolute; left: 450px; top: 690px; display: flex; align-items: center; gap: 14px; }
  .brand-mark { width: 90px; height: 90px; border-radius: 50%; background: var(--green-tab); }
  .brand-name { font-weight: 700; font-size: 27px; line-height: 32px; color: var(--green-tab); }
</style>
</head>
<body>
<main class="brochure">
  <div class="photo-backdrop" role="img" aria-label="Soft faded photograph of a smiling family group spanning the brochure background"></div>

  <!-- Column one -->
  <h2 class="tab" style="left:22px;top:57px;">WHO WE ARE</h2>
  <p class="body-text" style="left:48px;top:142px;width:290px;">A family driven lifestyle, recreation and leisure support service operated by a Management Committee consisting of parents and interested community members.</p>

  <h2 class="tab" style="left:22px;top:265px;">WHO WE ASSIST</h2>
  <h3 class="sub-head" style="left:48px;top:368px;">People with a disability who:</h3>
  <ul class="bullets" style="left:48px;top:390px;width:330px;">
    <li>are over the age of 16 years;</li>
    <li>reside in the Cairns region, from Gordonvale to Palm Cove;</li>
    <li>meet the Regional Disability Services eligibility criteria;</li>
    <li>are registered as Community Wellbeing Participation Agreement (CWPA) participants after rollout in Cairns in July 2018; and/or</li>
    <li>have their own financial resources.</li>
  </ul>

  <h2 class="tab tab--two-line" style="left:22px;top:604px;height:90px;">ROLE OF FAMILY/<br>ADVOCATE</h2>
  <p class="body-text" style="left:48px;top:718px;width:300px;">Families are our greatest resource and we actively seek their input to help the person with a disability maximize choice and control over their own lives.</p>

  <!-- Column two -->
  <h2 class="tab" style="left:421px;top:57px;">OUR PHILOSOPHY</h2>
  <h3 class="value-title" style="top:184px;">CHOICE</h3>
  <p class="value-text" style="top:236px;">Choice is a key element in lifestyle, recreation and leisure pursuits, and we tailor support to meet people's personal plans and goals.</p>
  <h3 class="value-title" style="top:349px;">INCLUSION</h3>
  <p class="value-text" style="top:401px;">We believe that supporting people individually is the best way to enable them to attain a valued role in their community.</p>
  <h3 class="value-title" style="top:514px;">OPPORTUNITY</h3>
  <p class="value-text" style="top:566px;">All people have the right to be part of their community and to experience life's opportunities.</p>
  <div class="brand">
    <span class="brand-mark"></span>
    <span class="brand-name">Bramblewood<br>Outings</span>
  </div>

  <!-- Column three -->
  <h2 class="tab" style="left:821px;top:57px;">HOW TO FIND US</h2>
  <h3 class="sub-head" style="left:843px;top:144px;">We assist people to:</h3>
  <ul class="bullets" style="left:845px;top:166px;width:330px;">
    <li>plan what support they need;</li>
    <li>choose suitable support people;</li>
    <li>accomplish daily living activities;</li>
    <li>participate in social and community activities;</li>
    <li>enhance and maintain independence, self confidence and self esteem;</li>
    <li>build capacity and improve or maintain skills;</li>
    <li>keep a job by supporting people in the work-place;</li>
    <li>improve lifelong learning;</li>
    <li>maintain health and wellbeing; and</li>
    <li>achieve their goals and desired outcomes.</li>
  </ul>
  <h3 class="sub-head" style="left:843px;top:428px;width:340px;">We employ support people to assist individuals:</h3>
  <ul class="bullets" style="left:845px;top:497px;width:330px;">
    <li>on a one to one ratio;</li>
    <li>in their home and in generic community settings;</li>
    <li>to implement their personal plan;</li>
    <li>to access community services; and</li>
    <li>to meet their changing needs.</li>
  </ul>
  <p class="note" style="left:843px;top:617px;width:310px;">We can provide 24 hour support but all support is in non-segregated settings.</p>

  <h2 class="tab" style="left:821px;top:672px;">HOW TO APPLY</h2>
  <p class="apply-text" style="left:843px;top:762px;width:310px;">Please contact our office to discuss how Bramblewood Outings can support you.</p>
</main>
</body>
</html>
```